Premium label design for product needed

UPDATE: (Scroll down)
For a face care product i need a new front label on the bottle. The current one is white and i want to add the franchise color green. The objective is to premiunize the packaging and to give guidance to the consumers to find their franchise color. The task is to find several option to color the label on the bottle in the most premium way. But at the same time it should not be playful, more in a serious medical direction or in a counterbrand direction. It should look absolutely premium. but should not shout to much. The text structure should remain the same. I will provide a powerpoint slide to illustrate the task even clearer.
UPDATE: DO NOT DESIGN THE FOLDING BOX, only design the bottle. The folding box only serves the purpose of giving the text/layout structure and rough color intent.

Target Market(s)

female 25-39

Requirements
Must have
• Premium, Uniqueness, Innovative

```html
<!DOCTYPE html>
<html lang="en">
<head>
<meta charset="utf-8">
<title>Pure Derma – Label Options</title>
<link href="https://fonts.googleapis.com/css2?family=EB+Garamond:wght@500&family=Patrick+Hand&display=swap" rel="stylesheet">
<style>
  :root {
    --canvas: #ebebeb;
    --strip: #ffffff;
    --cap: #d9d9d9;
    --cap-shade: #c4c4c4;
    --body: #f4f4f4;
    --body-edge: #e2e2e2;
    --franchise-green: #6dbb87;
    --ink: #222222;
    --label-ink: #333333;
  }
  * { margin: 0; padding: 0; box-sizing: border-box; }
  html, body { width: 1200px; height: 828px; overflow: hidden; }
  body { background: var(--strip); position: relative; font-family: "EB Garamond", serif; }
  .stage { position: absolute; left: 0; top: 0; width: 1200px; height: 800px; background: var(--canvas); }
  .bottle { position: absolute; width: 136px; }
  .bottle-cap {
    height: 146px;
    background: linear-gradient(90deg, var(--cap) 0%, #e6e6e6 40%, var(--cap-shade) 75%, var(--cap) 100%);
    border-bottom: 1px solid #cfcfcf;
  }
  .bottle-body {
    display: block; width: 136px; height: 301px;
    background: linear-gradient(90deg, var(--body-edge) 0%, var(--body) 35%, var(--body) 70%, var(--body-edge) 100%);
    border-radius: 0 0 8px 8px;
  }
  .label-mark { fill: var(--franchise-green); }
  .label-name { font-family: "EB Garamond", serif; font-weight: 500; font-size: 15px; fill: var(--ink); }
  .label-variant { font-family: "EB Garamond", serif; font-weight: 500; font-size: 9px; letter-spacing: 0.3px; fill: var(--label-ink); }
  .option-letter {
    position: absolute; top: 645px; width: 60px; text-align: center;
    font-family: "Patrick Hand", cursive; font-size: 36px; color: var(--ink);
  }
  .caption {
    position: absolute; left: 373px; top: 782px;
    font-family: "Patrick Hand", cursive; font-size: 32px; line-height: 1; color: #111111;
  }
</style>
</head>
<body>
  <div class="stage">
    <!-- Option E: square before the name -->
    <div class="bottle" style="left:177px; top:173px;">
      <div class="bottle-cap"></div>
      <svg class="bottle-body" viewBox="0 0 136 301">
        <rect class="label-mark" x="24" y="112" width="9" height="9"/>
        <text class="label-name" x="39" y="121">Pure Derma</text>
        <text class="label-variant" x="68" y="217" text-anchor="middle">R.L. MATTE FLUID</text>
      </svg>
    </div>
    <div class="option-letter" style="left:212px;">E</div>

    <!-- Option F: circle before the name -->
    <div class="bottle" style="left:411px; top:170px;">
      <div class="bottle-cap"></div>
      <svg class="bottle-body" viewBox="0 0 136 301">
        <circle class="label-mark" cx="29" cy="121" r="5"/>
        <text class="label-name" x="39" y="126">Pure Derma</text>
        <text class="label-variant" x="68" y="215" text-anchor="middle">R.L. MATTE FLUID</text>
      </svg>
    </div>
    <div class="option-letter" style="left:449px;">F</div>

    <!-- Option G: square after the name -->
    <div class="bottle" style="left:643px; top:167px;">
      <div class="bottle-cap"></div>
      <svg class="bottle-body" viewBox="0 0 136 301">
        <text class="label-name" x="22" y="124">Pure Derma</text>
        <rect class="label-mark" x="104" y="115" width="9" height="9"/>
        <text class="label-variant" x="68" y="219" text-anchor="middle">R.L. MATTE FLUID</text>
      </svg>
    </div>
    <div class="option-letter" style="left:682px;">G</div>

    <!-- Option H: circle after the name -->
    <div class="bottle" style="left:867px; top:163px;">
      <div class="bottle-cap"></div>
      <svg class="bottle-body" viewBox="0 0 136 301">
        <text class="label-name" x="22" y="123">Pure Derma</text>
        <circle class="label-mark" cx="109" cy="118" r="5"/>
        <text class="label-variant" x="68" y="216" text-anchor="middle">R.L. MATTE FLUID</text>
      </svg>
    </div>
    <div class="option-letter" style="left:913px;">H</div>
  </div>
  <p class="caption">Lorem ipsum</p>
</body>
</html>
```